Lakeport Cabinet Doors need 6 icons and 6 buttons

*** Two buttons to re-do
1. High end door change the red door for the one without color.
2. Two drawer fronts images together to make one. First maple then oak. Similar as the other buttons.

That's all.

Our company will start selling cabinet doors.
I need 6 icons and 6 buttons. Here are some general ideas:
All icon in the same row (5) should look alike!
All Buttons 6 of them should look alike!

4 buttons would be in the same row and two more buttons should be right underneath. Basically I was thinking to put one door for each button that represent each area.
I have two buttons underneath Drawer and Stain or Paint. These should look alike

Icons
1. Icon outside edge. See attachments for ideas. I like one of them because it look like maple. however look fake. and the other one I like the drawing show exactly the design but with those lines make them look like wood, but it doesn't have color. I like this one but with color to look like maple.
2. Wood type. 5 types. Oak, Maple, Cherry, Walnut, Mahogany. I was thinking to put one door on tap of the other one. Or five pieces of wood one next to the other.
3. Paint or Stain. 1/2 circle with 8 colorful colors and as a base 8 square stain colors. This icon should be same or very similar than button #6
4. Finish. Raw, satin, Semi and Gloss. One piece of wood with more shine in one side and almost not shine in the other end.
5. Dimensions. I would like a cabinet door with arrows. Arrows should be same color as the logo.
6. shopping cart. Something that show I am selling cabinet doors. Different from a regular shopping cart.

Buttons
I attached a muck up of the home page. I have 4 buttons and two buttons underneath.
1. High End Cabinets. see door with red Mahogany.
2. Raising panel. see Raw-wood-Calder
3. Flat panel. -Raw wood Tuscan
4. French lite
5. Drawer Fronts. It could be one single draw or several drawers at 45 degree each so it can fit several.
6. Stain or Paint should be the same or similar as the icon #3 that you will create but this one is a little bit longer. You already are doing this icon so you can use the same or create a new one but should be very close because both icon or button will open the same page.

That’s all.

I am attaching several jpgs one for the row of icons
one for the home page that include 6 buttons.
And logo.

Target Market(s)

We will be selling Kitchen cabinet doors. Most of my final customers will be women however because I sell raw wood doors then many contractors would be buying as well.

Industry/Entity Type

Shopping

Font styles to use
Sans Serif

Requirements
Must have
• all icons should looks similar
All buttons should looks similar
First 4 buttons is only one button with different picture.
Make all buttons and icons with a little dimension. See attachment (8 icons)
Nice to have
• If all icons and buttons look similar.
4 Buttons will be okay if they are exactly the same using the pictures that I provided. However it will be nice if they have small different each one. Very small difference is okay.
that will be nice if they use similar colors as the logo.

```html
<!DOCTYPE html>
<html lang="en">
<head>
<meta charset="utf-8">
<title>Lakeport Cabinet Doors – Buttons</title>
<link rel="stylesheet" href="https://fonts.googleapis.com/css2?family=Arimo:wght@400&display=swap">
<style>
  :root {
    --canvas: #ffffff;
    --bar: #3b3b3b;
    --bar-text: #f2f2f2;
    --accent: #e8872a;
    --caption: #333333;
    --maple-light: #ece2d3;
    --maple-mid: #ddd0bc;
    --maple-dark: #cdbca3;
    --maple-edge: #bfae95;
    --maple-shade: #d6c8b2;
    --oak-light: #e3c6a0;
    --oak-mid: #d5b286;
    --oak-dark: #c49d6e;
    --oak-edge: #b08552;
    --oak-shade: #cfa978;
  }
  * { box-sizing: border-box; margin: 0; padding: 0; }
  html, body {
    width: 1200px; height: 581px; overflow: hidden;
    background: var(--canvas);
    font-family: "Arimo", Arial, sans-serif;
  }
  .canvas { position: relative; width: 1200px; height: 581px; }

  .nav-button { position: absolute; display: block; text-decoration: none; }
  .nav-button__bar {
    position: absolute; left: 0; right: 0; z-index: 2;
    background: var(--bar);
    display: flex; align-items: center; justify-content: space-between;
    padding: 0 30px 0 23px;
    font-size: 13.5px; letter-spacing: 0.2px;
    color: var(--bar-text); text-transform: uppercase;
  }
  .nav-button__bar .accent { color: var(--accent); }
  .nav-button__arrow { width: 16px; height: 12px; display: block; }
  .nav-button__photo { position: absolute; left: 0; right: 0; overflow: hidden; }

  .photo--maple {
    background: radial-gradient(ellipse at 50% 55%, var(--maple-light) 0%, var(--maple-mid) 65%, var(--maple-dark) 100%);
  }
  .photo--oak {
    background: radial-gradient(ellipse at 50% 50%, var(--oak-light) 0%, var(--oak-mid) 60%, var(--oak-dark) 100%);
  }

  /* panel framing inside the photo areas */
  .panel { position: absolute; }
  .photo--maple .panel--frame {
    border: 6px solid var(--maple-shade);
    box-shadow: inset 0 0 0 1px var(--maple-edge), 0 0 0 1px var(--maple-edge);
  }
  .photo--maple .panel--raised {
    background: linear-gradient(180deg, var(--maple-light), var(--maple-mid));
    border: 1px solid var(--maple-edge);
    box-shadow: inset 0 0 0 14px rgba(205,188,163,0.35);
  }
  .photo--oak .panel--bevel {
    background: linear-gradient(180deg, var(--oak-light), var(--oak-mid));
    border: 1px solid var(--oak-edge);
    box-shadow: 0 2px 4px rgba(120,80,40,0.35);
  }
  .photo--oak .panel--step {
    background: linear-gradient(180deg, var(--oak-mid), var(--oak-light));
    border: 1px solid var(--oak-edge);
  }
  .photo--oak .panel--recess {
    background: var(--oak-shade);
    border: 1px solid var(--oak-edge);
    box-shadow: inset 0 3px 4px rgba(120,80,40,0.35);
  }

  /* High end cabinets */
  .button-high-end { left: 36px; top: 51px; width: 256px; height: 229px; }
  .button-high-end .nav-button__photo { top: 0; height: 186px; }
  .button-high-end .nav-button__bar { bottom: 0; height: 43px; }
  .button-high-end .panel--frame { left: 22px; top: 22px; right: 24px; bottom: -20px; }
  .button-high-end .panel--raised { left: 36px; top: 36px; right: 38px; bottom: -10px; }

  /* Drawer fronts options */
  .button-drawer { top: 303px; width: 548px; height: 194px; }
  .button-drawer .nav-button__bar { top: 0; height: 40px; padding-left: 28px; padding-right: 30px; }
  .button-drawer .nav-button__photo { top: 40px; bottom: 0; }
  .button-drawer--maple { left: 36px; }
  .button-drawer--oak { left: 615px; }

  .button-drawer--maple .panel--frame { left: 20px; top: 22px; right: 24px; bottom: -20px; }
  .button-drawer--maple .panel--raised { left: 64px; top: 50px; right: 66px; bottom: 20px; }

  .button-drawer--oak .panel--bevel { left: 52px; top: 14px; right: 40px; bottom: 6px; }
  .button-drawer--oak .panel--step { left: 78px; top: 42px; right: 70px; bottom: 36px; }
  .button-drawer--oak .panel--recess { left: 122px; top: 62px; right: 102px; bottom: 56px; }

  .option-caption {
    position: absolute; top: 506px; width: 200px;
    text-align: center; font-size: 17.5px; color: var(--caption);
  }
  .option-caption--one { left: 211px; }
  .option-caption--two { left: 789px; }
</style>
</head>
<body>
<main class="canvas">

  <a class="nav-button button-high-end" href="#high-end-cabinets">
    <div class="nav-button__photo photo--maple" role="img" aria-label="Raw maple raised panel cabinet door with rope moulding">
      <div class="panel panel--frame"></div>
      <div class="panel panel--raised"></div>
    </div>
    <div class="nav-button__bar">
      <span>High end <span class="accent">cabinets</span></span>
      <svg class="nav-button__arrow" viewBox="0 0 16 12" aria-hidden="true">
        <path d="M1 1 L7 6 L1 11 Z M8 1 L14 6 L8 11 Z" fill="#ffffff"/>
      </svg>
    </div>
  </a>

  <a class="nav-button button-drawer button-drawer--maple" href="#drawer-fronts">
    <div class="nav-button__bar">
      <span>Drawer <span class="accent">fronts</span></span>
      <svg class="nav-button__arrow" viewBox="0 0 16 12" aria-hidden="true">
        <path d="M1 1 L7 6 L1 11 Z M8 1 L14 6 L8 11 Z" fill="#ffffff"/>
      </svg>
    </div>
    <div class="nav-button__photo photo--maple" role="img" aria-label="Raw maple raised panel drawer front with rope moulding">
      <div class="panel panel--frame"></div>
      <div class="panel panel--raised"></div>
    </div>
  </a>
  <p class="option-caption option-caption--one">Option1</p>

  <a class="nav-button button-drawer button-drawer--oak" href="#drawer-fronts">
    <div class="nav-button__bar">
      <span>Drawer <span class="accent">fronts</span></span>
      <svg class="nav-button__arrow" viewBox="0 0 16 12" aria-hidden="true">
        <path d="M1 1 L7 6 L1 11 Z M8 1 L14 6 L8 11 Z" fill="#ffffff"/>
      </svg>
    </div>
    <div class="nav-button__photo photo--oak" role="img" aria-label="Raw oak raised panel drawer front">
      <div class="panel panel--bevel"></div>
      <div class="panel panel--step"></div>
      <div class="panel panel--recess"></div>
    </div>
  </a>
  <p class="option-caption option-caption--two">Option2</p>

</main>
</body>
</html>
```